Website redesign for a Cloud Advisory business

We are looking to revisit our existing brand and website, with a view to updating both. Looking for concepts and designs for how the website might look, flow and feel. Current website is: www.brellomint.com.au

Scope and Deliverables: Concept design for the home page and one internal page.

We do not expect you to design all the pages and all the elements of the website at this stage.

This job is not for the full website design, but just for concepts that we can start with when we go into the full website design.

We would love to see a design feature based on our name, logo, or industry, which can run through banners and other collateral (twitter banner, ads on Google, corporate documents etc).

We want the brand to properly depict what we bring/deliver to businesses when consulting to them and this should extend to the colour scheme, logo, font (perhaps updated) and copy (which will be supplied).

Our brand should suitably communicate our ability, knowledge and extensive experience within the Cloud space.

It should express and evoke credibility, knowledge and understanding of the Cloud space, independence, gravitas, reliability, efficiency, trust, expertise, approachability, service delivery but be uncomplicated, practical and use plain speaking language.

Colours that reinforce this might include: Blues, blacks, silver, white, grey and our existing orange.

Website designs that we like or have referenced include:

Varnolift: http://varnolift.com.au/ - This has good information but looks a little amateur in it’s cartoon like design and colour scheme. Also, this seems to be aimed at clients more interested in price than design and what we are going for is a little more high end.

Pendramoor: https://www.pendramoor.com.au/ - This site has merit in its’ setup but little call to action on the home page, especially before the scroll line. I like the set up of the Case Studies page however I’d look to make it more prominent by having it set up 3 across rather than the 4 they have. Something such as this: https://www.qandelby.com/case-studies

Tolvane: http://www.tolvane.com.au/#home4 - This page is a good one as far as selling services and information on the company. I quite like it.

MirefoldIT: http://www.mirefoldit.com.au/ - While I don’t think is particularly creative, it does practically depict the services we offer in a fairly clear way and might be a bit of a basic (albeit dull) template to follow.

JDP: https://store.jdp.com/us/Product-Family/JDP-Advisory-Services/JDP-Cloud-Advisory-Service/p/JDP-Services-Cloud-Advisory - This offers substantial information but is probably a little confusing although the roll-over drop down menus have merit.

ZEV: http://www.zev.net.au/en/services/ - While this in not quite what we are looking for, the colour scheme gives it more gravitas and quality.

As another reference, this website and the way they present their case studies is also something we like, although I’d like them shown 3 up, side by side…. https://www.qandelby.com/case-studies.

We have added a page layout and page purpose document.

Target Market(s)

Corporates, small - medium business, direct referrals, via search results

Industry/Entity Type

Business

Number of Pages Required

1 page

Font styles to use
Sans Serif

Colors
85abd2
0455a3
000000
f37122
5c5c5c

Requirements
Must have
• Website must be mobile device compatible.
• Concept design for the home page.
Nice to have
• We would love to see a design feature based on our name, logo, or industry, which can run through banners and other collateral (twitter banner, ads on Google, corporate documents etc).

```html
<!DOCTYPE html>
<html lang="en">
<head>
<meta charset="utf-8">
<title>Brellomint – Impartial Cloud Solutions</title>
<link href="https://fonts.googleapis.com/css2?family=Glegoo:wght@400;700&family=Open+Sans:wght@400;600;700&family=Raleway:wght@400;700&display=swap" rel="stylesheet">
<style>
:root{
  --orange:#f15a22;
  --ink:#2b2b2b;
  --dark:#333333;
  --footer:#2e2e2e;
  --grey:#5c5c5c;
  --line:#d8d8d8;
  --white:#ffffff;
  --blue:#2a35c9;
}
*{margin:0;padding:0;box-sizing:border-box}
html,body{width:1200px;height:3130px;overflow:hidden}
body{font-family:"Open Sans",Arial,sans-serif;color:var(--grey);background:var(--white);position:relative}
.serif{font-family:"Glegoo",Georgia,serif}
section,header,footer{position:absolute;left:0;width:1200px}
.center{text-align:center}

/* hero */
.hero{top:0;height:810px;overflow:hidden}
.hero-photo{position:absolute;inset:0;background:linear-gradient(180deg,#3d4a5c 0%,#5d6a7a 35%,#6d6a66 60%,#3a3430 100%)}
.hero-photo::after{content:"";position:absolute;inset:0;background:radial-gradient(ellipse 260px 420px at 600px 520px,rgba(20,20,24,.75),rgba(20,20,24,0))}
.logo{position:absolute;left:48px;top:26px;display:flex;align-items:center;gap:10px}
.logo-mark{width:40px;height:40px;background:var(--orange)}
.logo-name{font-weight:700;font-size:34px;color:var(--white);letter-spacing:1px}
.nav{position:absolute;top:110px;left:0;width:1200px;height:46px;background:var(--orange);display:flex;padding-left:48px}
.nav a{color:var(--white);text-decoration:none;font-size:13.5px;font-weight:600;line-height:46px;padding:0 18px}
.nav a.active{background:var(--ink)}
.hero-title{position:absolute;top:362px;left:0;width:100%;font-size:44px;font-weight:400;color:var(--white);letter-spacing:1px}
.hero-sub{position:absolute;top:440px;left:0;width:100%;font-size:17.5px;line-height:26px;color:#eee}
.btn{position:absolute;display:flex;align-items:center;justify-content:center;color:var(--white);text-decoration:none}
.btn-hero{left:455px;top:543px;width:292px;height:54px;background:var(--orange);border-radius:4px;font-family:"Raleway",sans-serif;font-weight:700;font-size:23px}

/* services */
.services{top:810px;height:505px}
.section-title{font-size:37px;color:var(--ink);font-weight:700;letter-spacing:1px}
.services .section-title{position:absolute;top:42px;left:0;width:100%}
.services .lead{position:absolute;top:98px;left:0;width:100%;font-size:15px;color:#444}
.service{position:absolute;top:150px;width:220px;text-align:center}
.service svg{display:block;margin:0 auto}
.service h3{font-family:"Glegoo",serif;font-weight:400;font-size:18.5px;color:var(--ink);line-height:18px;margin-top:22px;height:40px}
.service p{font-size:12.5px;line-height:20px;color:#555;margin-top:2px}

/* band */
.band{top:1315px;height:292px;background:var(--orange);color:var(--white)}
.band h2{position:absolute;top:34px;left:0;width:100%;font-size:37px;font-weight:700;letter-spacing:1px}
.band .tag{position:absolute;top:88px;left:0;width:100%;font-size:35px;line-height:48px;font-weight:400}
.btn-dark{left:463px;top:206px;width:253px;height:49px;background:var(--dark);font-family:"Glegoo",serif;font-size:22px;border-radius:3px}

/* about */
.about{top:1607px;height:370px}
.about-title{position:absolute;top:42px;left:0;width:100%;font-family:"Raleway",sans-serif;font-weight:700;font-size:37px;color:var(--orange)}
.about-sub{position:absolute;top:96px;left:0;width:100%;font-family:"Raleway",sans-serif;font-size:27px;color:#555}
.divider{position:absolute;top:145px;left:370px;width:460px;height:1px;background:var(--line)}
.dots{position:absolute;top:138px;left:570px;width:60px;display:flex;justify-content:center;gap:6px}
.dots i{width:6px;height:6px;border-radius:50%;background:var(--orange)}
.about-text{position:absolute;left:150px;width:900px;font-size:14.5px;line-height:26px;color:#444;text-align:center}

/* testimonials */
.testimonials{top:1977px;height:458px;overflow:hidden}
.testi-photo{position:absolute;inset:0;background:linear-gradient(100deg,#2a2a2a 0%,#4a4a4a 40%,#5c5c5c 70%,#3a3a3a 100%)}
.testimonials h2{position:absolute;top:34px;left:0;width:100%;font-size:31px;color:var(--white);font-weight:400}
.quote-mark{position:absolute;left:561px;top:108px}
.testimonials blockquote{position:absolute;top:220px;left:100px;width:1000px;text-align:center;color:var(--white);font-size:14.5px;line-height:25px;font-weight:600}
.written{position:absolute;top:322px;left:0;width:100%;color:var(--white);font-size:13.5px;font-weight:700;line-height:22px}
.slides{position:absolute;top:402px;left:501px;display:flex;gap:6px}
.slides i{width:36px;height:5px;background:#ddd}
.slides i.on{background:#2a6dc9}

/* cta */
.cta{top:2435px;height:305px;background:var(--orange);color:var(--white)}
.cta h2{position:absolute;top:45px;left:0;width:100%;font-size:33px;font-weight:400}
.cta p{position:absolute;top:112px;left:300px;width:600px;font-size:16px;line-height:32px;color:#fff}
.btn-cta{left:445px;top:207px;width:365px;height:50px;background:var(--dark);border-radius:4px;font-family:"Glegoo",serif;font-size:21px;gap:40px}

/* footer */
.site-footer{top:2740px;height:332px;background:var(--footer);color:var(--white)}
.col{position:absolute;top:48px}
.col h4{font-family:"Raleway",sans-serif;font-weight:400;font-size:30px;margin-bottom:20px}
.col ul{list-style:none}
.col li{font-size:14px;line-height:30px;font-family:Arial,sans-serif}
.col li::before{content:"→";margin-right:12px;font-size:12px}
.socials{display:flex;gap:12px}
.socials span{width:32px;height:32px;border-radius:50%;border:2px solid #ddd}
.newsletter .news-title{margin-top:26px;font-size:28px;margin-bottom:14px}
.input{width:190px;height:32px;background:#fff;color:#999;font-size:12px;line-height:32px;padding-left:10px}
.submit{margin-top:12px;width:86px;height:26px;background:var(--orange);font-size:12px;font-weight:700;text-align:center;line-height:26px}
.contact-row{display:flex;gap:16px;align-items:flex-start;margin-bottom:18px}
.contact-row .ico{width:26px;height:26px;border-radius:50%;background:var(--orange);flex:none;display:flex;align-items:center;justify-content:center}
.contact-row b{font-size:16px;font-family:Arial,sans-serif}
.contact-row small{display:block;font-size:12px;line-height:18px;margin-top:4px;font-family:Arial,sans-serif;font-weight:600}
.copyright{position:absolute;left:0;width:1200px;top:3072px;height:58px;background:var(--orange);color:var(--white);font-size:13px;line-height:58px;text-align:center}
</style>
</head>
<body>

<header class="hero">
  <div class="hero-photo" role="img" aria-label="Photograph of a businessman opening his shirt against a cloudy sky"></div>
  <div class="logo"><span class="logo-mark"></span><span class="logo-name">BRELLOMINT</span></div>
  <nav class="nav">
    <a class="active">Home</a><a>About Us</a><a>Industry Specialties</a><a>Solutions</a><a>The Company We Keep</a><a>Case Studies &amp; Testimonials</a><a>FAQ's</a><a>Blog</a><a>Contact Us</a>
  </nav>
  <h1 class="hero-title serif center">IMPARTIAL CLOUD SOLUTIONS</h1>
  <p class="hero-sub center">Throw away all your confusing indicators and learn the simple techniques that<br>make the classics just as effective today as they were 100 years ago</p>
  <a class="btn btn-hero">Get Started Free</a>
</header>

<section class="services">
  <h2 class="section-title serif center">OUR CLOUD SERVICES</h2>
  <p class="lead center serif">Pendramoor provides unrivalled cloud advisory and technology services for the world's leading brands.</p>

  <div class="service" style="left:28px">
    <svg width="124" height="124" viewBox="0 0 124 124"><path d="M62 4a58 58 0 1 1-30 107l-22 9 6-22A58 58 0 0 1 62 4z" fill="#f15a22"/><circle cx="62" cy="62" r="36" fill="#fff"/><path d="M62 46c7 10 11 16 11 21a11 11 0 0 1-22 0c0-5 4-11 11-21z" fill="#f15a22"/><path d="M58 4h8v18h-8z" fill="#fff"/></svg>
    <h3>System Selection</h3>
    <p>dolore magna aliqua. Ut enim ad minim veniam, quis nostrud exercitation ullamco laboris nisi ut adolore magna aliqua magna aliq.</p>
  </div>
  <div class="service" style="left:262px">
    <svg width="124" height="124" viewBox="0 0 124 124"><circle cx="62" cy="62" r="48" fill="none" stroke="#3a3a3a" stroke-width="22"/><path d="M58 2h8v22h-8z" fill="#fff"/><circle cx="62" cy="62" r="32" fill="#fff"/><path d="M50 76c0-18 10-26 26-28-2 16-10 26-26 28zm0 0l14-14" fill="#3a3a3a" stroke="#3a3a3a" stroke-width="2"/></svg>
    <h3>Accounting Systems &amp; Conversions</h3>
    <p>dolore magna aliqua. Ut enim ad minim veniam, quis nostrud exercitation ullamco laboris nisi ut adolore magna aliqua magna aliq.</p>
  </div>
  <div class="service" style="left:483px">
    <svg width="124" height="124" viewBox="0 0 124 124"><circle cx="62" cy="62" r="48" fill="none" stroke="#3a3a3a" stroke-width="22"/><path d="M58 2h8v22h-8z" fill="#fff"/><circle cx="62" cy="62" r="32" fill="#fff"/><rect x="44" y="48" width="36" height="24" rx="2" fill="none" stroke="#3a3a3a" stroke-width="4"/><path d="M56 78h12" stroke="#3a3a3a" stroke-width="4"/></svg>
    <h3>Integration</h3>
    <p>dolore magna aliqua. Ut enim ad minim veniam, quis nostrud exercitation ullamco laboris nisi ut adolore magna aliqua magna aliq.</p>
  </div>
  <div class="service" style="left:704px">
    <svg width="124" height="124" viewBox="0 0 124 124"><circle cx="62" cy="62" r="48" fill="none" stroke="#3a3a3a" stroke-width="22"/><path d="M58 2h8v22h-8z" fill="#fff"/><circle cx="62" cy="62" r="32" fill="#fff"/><path d="M62 44a12 12 0 0 1 7 22v6h-14v-6a12 12 0 0 1 7-22zM56 78h12" fill="none" stroke="#3a3a3a" stroke-width="4"/></svg>
    <h3>Business Inventory</h3>
    <p>dolore magna aliqua. Ut enim ad minim veniam, quis nostrud exercitation ullamco laboris nisi ut adolore magna aliqua magna aliq.</p>
  </div>
  <div class="service" style="left:925px">
    <svg width="124" height="124" viewBox="0 0 124 124"><circle cx="62" cy="62" r="48" fill="none" stroke="#3a3a3a" stroke-width="22"/><path d="M58 2h8v22h-8z" fill="#fff"/><circle cx="62" cy="62" r="32" fill="#fff"/><rect x="48" y="50" width="26" height="26" fill="none" stroke="#3a3a3a" stroke-width="4"/><path d="M54 62l6 6 14-16" fill="none" stroke="#3a3a3a" stroke-width="4"/></svg>
    <h3>Business Project &amp; Job Management</h3>
    <p>dolore magna aliqua. Ut enim ad minim veniam, quis nostrud exercitation ullamco laboris nisi ut adolore magna aliqua magna aliq.</p>
  </div>
</section>

<section class="band">
  <h2 class="serif center">IMPARTIAL CLOUD SOLUTIONS</h2>
  <p class="tag serif center">The Idea Of Concierge Services Into<br>Lifestyle Management</p>
  <a class="btn btn-dark">Learn more</a>
</section>

<section class="about">
  <h2 class="about-title center">ABOUT COMPANY</h2>
  <p class="about-sub center">Design for Urban Pioneers</p>
  <div class="divider"></div>
  <div class="dots"><i></i><i></i><i></i></div>
  <p class="about-text" style="top:172px">BRELLOMINT &amp; Co is dedicated to providing assistance to busy Chicago families.Mara Quill, the founder &amp; principal, began her career as a teacher and nanny. She moved from Seattle to Chicago to take on the role as a House Manager. Serving in that role for 13 years, she understands the high demands life puts on us all. She has developed long and lasting relationships with vendors to assist in completing any project. Need help? Call Mara Quill &amp; Co.</p>
  <p class="about-text" style="top:284px">There is no task too small or too large that we aren't willing to take on!</p>
</section>

<section class="testimonials">
  <div class="testi-photo" role="img" aria-label="Photograph of a hand holding a tablet in a busy office lobby"></div>
  <h2 class="serif center">Our Testimonials</h2>
  <svg class="quote-mark" width="80" height="80" viewBox="0 0 80 80"><circle cx="40" cy="40" r="38" fill="#2a35c9" stroke="#fff" stroke-width="4"/><path d="M26 34h12v12c0 6-4 9-9 10v-4c3-1 4-3 4-6h-7zM44 34h12v12c0 6-4 9-9 10v-4c3-1 4-3 4-6h-7z" fill="#fff"/></svg>
  <blockquote>"Korvala help us to find new potential customers and also to deepen existing customer relationships. Scent desire to customize exactly to our needs service tool has been ihaltavaa "Korvala help us to find new potential customers and also to deepen existing customer relationships. Scent desire to customize exactly to our needs service tool has been ihaltavaa""</blockquote>
  <div class="written center">Written By<br>EERO SALMENKIVI, SALES MANAGER, HOLTRANE LTD</div>
  <div class="slides"><i class="on"></i><i></i><i></i><i></i><i></i></div>
</section>

<section class="cta">
  <h2 class="serif center">Call us today at 1300 472 918</h2>
  <p class="serif center">Lets us show you how we can take your trading to the next level. you can also email us as at info@brellomint.com.au</p>
  <a class="btn btn-cta">Start My FREE Membership <span>›</span></a>
</section>

<footer class="site-footer">
  <div class="col" style="left:119px">
    <h4>Quick links</h4>
    <ul><li>Home</li><li>Services</li><li>Carriers</li><li>Investors</li><li>About</li><li>Contact us</li></ul>
  </div>
  <div class="col" style="left:334px">
    <h4>Services</h4>
    <ul><li>Etusivu</li><li>Yritys &amp; Palvelut</li><li>Referenssit</li><li>Yhteystiedot</li><li>Lähetä tarjouspyyntö</li></ul>
  </div>
  <div class="col newsletter" style="left:568px">
    <h4>Follow Us</h4>
    <div class="socials"><span></span><span></span><span></span><span></span></div>
    <h4 class="news-title">Newsletter</h4>
    <div class="input">Email Address</div>
    <div class="submit">SUBMIT</div>
  </div>
  <div class="col" style="left:864px;width:270px">
    <h4>Contact Details</h4>
    <div class="contact-row"><span class="ico"><svg width="12" height="14" viewBox="0 0 12 14"><path d="M6 0a5 5 0 0 1 5 5c0 4-5 9-5 9S1 9 1 5a5 5 0 0 1 5-5z" fill="#fff"/></svg></span><div><b>BRELLOMINT</b><small>simply dummy text of the printing and typesetting industry. Lorem Ipsum has been the industry's</small></div></div>
    <div class="contact-row"><span class="ico"><svg width="14" height="14" viewBox="0 0 14 14"><path d="M3 1l3 3-2 2c1 2 2 3 4 4l2-2 3 3-2 2C6 13 1 8 1 3z" fill="#fff"/></svg></span><b style="line-height:26px;font-size:20px">1300 472 918</b></div>
    <div class="contact-row"><span class="ico"><svg width="14" height="10" viewBox="0 0 14 10"><rect width="14" height="10" fill="#fff"/><path d="M0 0l7 6 7-6" fill="none" stroke="#f15a22" stroke-width="1.5"/></svg></span><small style="line-height:26px;margin:0;font-size:14px">info@brellomint.com.au</small></div>
  </div>
</footer>
<div class="copyright">Copyright BRELLOMINT © 2016. All Rights Reserved.</div>

</body>
</html>
```